PixelGuild CEO Needs a Graphic for a Blog About Crowdsourcing and Online Employment

We need a simple graphic / banner for a blog post that's going to be posted on a large publication (like ByteHerald, Marlowe Commerce Quarterly).

The article will be written by Bram Ostiver (PixelGuild's CEO) and the title will be "Why Websites Will Become the Biggest Employers in the World". The article is about why online employers (like PixelGuild and Tasklynx) will one day have more 'workers' than offline employers.

We'd really like to get this ASAP - so early submissions encouraged. We will try and get the winning designer linked to from the article.

Note that this brief is similar to a previous project that we ran http://jobs.pixelguild-example.com/job.aspx?id=58213 where the article and design was published on ByteHerald http://byteherald-example.com/2012/12/08/asias-hidden-gig-surge/ and the designer (Moravia) was linked to from ByteHerald.

Target Market(s)

Entrepreneurs, journalists, small business owners, tech people.

Industry/Entity Type

Business

Requirements
Must have
• The graphic SHOULD have:
1) Have the text "Why Websites Will Become the Biggest Employers in the World" with some nice design and fonts (consider grey subtle pattern background and white drop shadow on fonts) - see attached examples
2) Have the dimensions 640px wide by 240px wide
Nice to have
• The graphic COULD have:

1) Incorporate the following words in the background (like a word cloud): crowdsource, microtask, crowdfund, witkey, outsource, freelance, online, work from home

OR

2) Incorporate logos of new online employers (Tasklynx, vYard, PixelGuild, ChoreFinch, Lunqiaofu, ClockworkPawn, Frameharbor) into the design. If the background of the graphic is grey, ideally, these logos would also be greyscale i.e. they should form a background motif.

OR

3) Show some graphic communicating themes from the article e.g. laptop, globe, workers, connections across the globe

OR

4) Have a second line of text "Why Crowdsourcing Websites Will Overtake Traditional Employers"
Should not have
• Should NOT have:
1) Any photos or clipart

```html
<!DOCTYPE html>
<html lang="en">
<head>
<meta charset="utf-8">
<title>Why Websites Will Become the Biggest Employers in the World</title>
<link rel="stylesheet" href="https://fonts.googleapis.com/css2?family=Montserrat:wght@700;800&display=swap">
<style>
  :root {
    --bg: #e8e9ea;
    --band-top: #ffffff;
    --band-bottom: #d9dadb;
    --ink-dark: #343434;
    --ink-grey: #6b6b6b;
    --accent: #1f6a8f;
    --figure-blue: #0f3b73;
    --figure-grey: #3b3b3b;
    --map-blue: #c9dcef;
    --map-grey: #d6d6d6;
    --chevron: #5f7f8e;
  }
  html, body {
    margin: 0;
    padding: 0;
    overflow: hidden;
    background: var(--bg);
  }
  .banner {
    position: relative;
    width: 1200px;
    height: 450px;
    overflow: hidden;
    background: var(--bg);
    font-family: "Montserrat", "Century Gothic", sans-serif;
  }
  .world-map {
    position: absolute;
    border-radius: 40% 45% 35% 40%;
  }
  .world-map--east {
    left: 440px;
    top: 80px;
    width: 760px;
    height: 370px;
    background: radial-gradient(ellipse at 55% 50%, var(--map-blue) 0%, rgba(201,220,239,0.6) 60%, rgba(232,233,234,0) 80%);
  }
  .world-map--west {
    left: -60px;
    top: 190px;
    width: 560px;
    height: 280px;
    background: radial-gradient(ellipse at 50% 45%, var(--map-grey) 0%, rgba(214,214,214,0.5) 60%, rgba(232,233,234,0) 80%);
  }
  .title-band {
    position: absolute;
    left: 0;
    top: 0;
    width: 1200px;
    height: 220px;
  }
  .headline {
    position: absolute;
    left: 0;
    top: 0;
    width: 1200px;
    margin: 0;
    text-align: center;
    font-weight: 800;
    text-transform: uppercase;
    color: var(--ink-dark);
    text-shadow: 0 2px 0 rgba(255,255,255,0.9);
    letter-spacing: 1px;
  }
  .headline__line {
    position: absolute;
    left: 0;
    width: 100%;
    line-height: 1;
    white-space: nowrap;
  }
  .headline__line--one { top: 16px; font-size: 40px; }
  .headline__line--two { top: 72px; font-size: 54px; }
  .headline__line--three { top: 130px; font-size: 36px; }
  .headline__key { font-size: 56px; color: var(--accent); }
  .headline__world { font-size: 54px; color: var(--ink-grey); }
  .worker {
    position: absolute;
    top: 238px;
    width: 52px;
    height: 130px;
    border-radius: 24px 24px 6px 6px;
  }
  .worker--offline { left: 242px; background: var(--figure-grey); }
  .worker--online { background: var(--figure-blue); }
  .worker--a { left: 517px; }
  .worker--b { left: 709px; }
  .worker--c { left: 898px; }
  .comparison {
    position: absolute;
    left: 376px;
    top: 274px;
    width: 50px;
    height: 60px;
  }
  .worker-label {
    position: absolute;
    top: 388px;
    width: 80px;
    margin: 0;
    text-align: center;
    font-size: 32px;
    font-weight: 800;
    line-height: 1;
  }
  .worker-label--offline { left: 228px; color: var(--ink-grey); }
  .worker-label--online { color: var(--accent); }
  .worker-label--a { left: 503px; }
  .worker-label--b { left: 695px; }
  .worker-label--c { left: 884px; }
</style>
</head>
<body>
<div class="banner">
  <div class="world-map world-map--west" role="img" aria-label="Grey world map, western hemisphere"></div>
  <div class="world-map world-map--east" role="img" aria-label="Light blue world map, eastern hemisphere"></div>

  <svg class="title-band" viewBox="0 0 1200 220" aria-hidden="true">
    <defs>
      <linearGradient id="bandFill" x1="0" y1="0" x2="0" y2="1">
        <stop offset="0" stop-color="var(--band-top)" stop-opacity="0.95"/>
        <stop offset="0.75" stop-color="var(--band-top)" stop-opacity="0.6"/>
        <stop offset="1" stop-color="var(--band-bottom)" stop-opacity="0.9"/>
      </linearGradient>
    </defs>
    <path d="M0 0 H1200 V120 Q600 250 0 120 Z" fill="url(#bandFill)"/>
  </svg>

  <h1 class="headline">
    <span class="headline__line headline__line--one">Why <span class="headline__key">Websites</span> will become</span>
    <span class="headline__line headline__line--two">The biggest employers</span>
    <span class="headline__line headline__line--three">In the <span class="headline__world">World</span></span>
  </h1>

  <div class="worker worker--offline" role="img" aria-label="Grey worker pictogram"></div>
  <svg class="comparison" viewBox="0 0 50 60" aria-label="Less than">
    <path d="M44 4 L8 30 L44 56" fill="none" stroke="var(--chevron)" stroke-width="12" stroke-linejoin="miter"/>
  </svg>
  <div class="worker worker--online worker--a" role="img" aria-label="Blue worker pictogram"></div>
  <div class="worker worker--online worker--b" role="img" aria-label="Blue worker pictogram"></div>
  <div class="worker worker--online worker--c" role="img" aria-label="Blue worker pictogram"></div>

  <p class="worker-label worker-label--offline">W</p>
  <p class="worker-label worker-label--online worker-label--a">W</p>
  <p class="worker-label worker-label--online worker-label--b">W</p>
  <p class="worker-label worker-label--online worker-label--c">W</p>
</div>
</body>
</html>
```